Wenna's Atelier, Beauty & Therapy. New business in Verbier, Switzerland

Simple Flyer to put in evidence a particular service that the studio offers that is
EMS ( ELECTRIC MUSCLE STIMULATION)
There is a bike festival in Verbier ion the 12th of August and i would like to take an opportunity of this slot to advertise our new suit of EMS that can be very helpful for bike riders. The product is a suit with muscle electrostimulation, And there are many advantages and functionnality. For sportsmen and women, it can
I don't have any particular picture be cause the product is very new.
But i can send you some images for you to understand what it is, but if you find some images on the web it is better :)
I upload different versions of Logo, PLEASE FEEL FREE TO CHOOSE WHAT IS BEST :)
please check this link for more information about the product applied for bikers
https://www.pulvaro-suits.example/en/cycling-training-with-muscle-electrostimulation/
Updates
Hello Designers,
Here are a few details concerning the project;
- Wenna's Atelier is not a reseller of the EMS suits, but we provide it as a service inside our studio.
- We wish to communicate on this new technology in order to bring a maximum of attention, not only for the suit, but also for the brand it self, since it is new in Verbier.
- for the flyer, i would like it to be simple, appealing, and without too much text.
- a french version of the same flyer is appreciated, without extra cost ;)
Thanks
Hello all designers,
thank you for all the good work.
For you who mentioned a date for the festival, i suggest please to take it off, and keep only " Alpen Pedal Gathering" if you want.
Thank you

```html
<!DOCTYPE html>
<html lang="en">
<head>
<meta charset="utf-8">
<title>Wenna's Atelier – EMS Flyer</title>
<link href="https://fonts.googleapis.com/css2?family=Poppins:wght@400;600;700;800&display=swap" rel="stylesheet">
<style>
  :root{
    --plum:#7b1b6f;
    --plum-deep:#5c1253;
    --blush:#f8e3df;
    --slate:#7a7a7a;
    --teal:#2a9ca7;
    --icon-grey:#8d8d8d;
    --caption:#7a7a7a;
    --ink:#3a3a3a;
    --paper:#ffffff;
    --backdrop:#ececec;
  }
  *{margin:0;padding:0;box-sizing:border-box}
  html,body{width:1200px;height:2954px;overflow:hidden}
  body{background:var(--backdrop);font-family:'Poppins',sans-serif;position:relative}
  .flyer{position:absolute;left:110px;top:842px;width:980px;height:1270px;background:var(--paper);overflow:hidden;box-shadow:0 6px 24px rgba(0,0,0,.18)}
  .flyer-shapes{position:absolute;inset:0}
  .abs{position:absolute}
  .brand-mark{left:29px;top:37px;width:264px;height:264px;display:flex;flex-direction:column;align-items:center;justify-content:center;gap:14px}
  .brand-dot{width:46px;height:46px;border-radius:50%;background:var(--plum)}
  .brand-name{font-weight:600;font-size:22px;letter-spacing:2px;color:var(--plum);text-transform:uppercase}
  .headline{right:50px;top:56px;width:600px;text-align:right;color:#fff;font-weight:700;line-height:1.18}
  .headline .line-a{font-size:34px;display:block}
  .headline .line-b{font-size:45px;display:block}
  .offer-lead{left:54px;top:330px;font-weight:600;font-size:38px;line-height:1.05;color:var(--ink);text-transform:uppercase}
  .ems-word{left:50px;top:400px;font-weight:800;font-size:158px;line-height:1;letter-spacing:-4px;color:var(--plum)}
  .ems-full{left:54px;top:566px;font-weight:700;font-size:39px;line-height:1.1;color:var(--ink);text-transform:uppercase}
  .festival-title{left:276px;width:651px;top:708px;text-align:center;color:#fff;font-weight:600;font-size:35px;line-height:1.2}
  .festival-name{left:346px;width:480px;top:761px;height:62px;display:flex;align-items:center;justify-content:center;color:#fff;font-weight:700;font-size:36px;letter-spacing:.5px;text-transform:uppercase;white-space:nowrap}
  .festival-note{left:280px;width:640px;top:840px;text-align:center;color:#fff;font-size:21px;line-height:1.3}
  .feature{width:220px;text-align:center;color:var(--caption);font-size:19px;line-height:1.22;top:1044px}
  .site-url{left:0;width:980px;top:1198px;text-align:center;color:#fff;font-size:40px;font-weight:400;line-height:1.2}
</style>
</head>
<body>
<div class="flyer">
  <svg class="flyer-shapes" width="980" height="1270" viewBox="0 0 980 1270">
    <defs>
      <linearGradient id="plumGrad" x1="0" y1="0" x2="1" y2="1">
        <stop offset="0" stop-color="#8a2380"/>
        <stop offset="1" stop-color="#5c1253"/>
      </linearGradient>
      <linearGradient id="photoGrad" x1="0" y1="0" x2="0" y2="1">
        <stop offset="0" stop-color="#eeeaec"/>
        <stop offset="1" stop-color="#56565c"/>
      </linearGradient>
      <linearGradient id="suitGrad" x1="0" y1="0" x2="0" y2="1">
        <stop offset="0" stop-color="#2b2e33"/>
        <stop offset="1" stop-color="#15171b"/>
      </linearGradient>
    </defs>
    <polygon points="0,0 440,0 0,170" fill="var(--blush)"/>
    <path d="M390,0 L980,0 L980,575 C900,430 760,250 560,215 C450,198 330,200 255,210 C300,130 340,55 390,0 Z" fill="url(#plumGrad)"/>
    <path d="M262,208 C450,180 660,200 980,390" fill="none" stroke="#fff" stroke-width="7"/>
    <circle cx="161" cy="169" r="134" fill="#fff" stroke="var(--plum)" stroke-width="6"/>
    <rect x="450" y="262" width="490" height="434" rx="8" fill="url(#photoGrad)" opacity=".5" role="img" aria-label="Photo of three people wearing EMS training suits beside a control tablet on a stand"/>
    <circle cx="149" cy="1006" r="143" fill="#8f8f8f"/>
    <path d="M276,696 H905 a22,22 0 0 1 22,22 V828 H276 Z" fill="var(--slate)"/>
    <path d="M276,826 H927 V890 a22,22 0 0 1 -22,22 H306 a30,30 0 0 1 -30,-30 Z" fill="var(--teal)"/>
    <rect x="346" y="761" width="480" height="62" rx="6" fill="var(--plum)"/>
    <rect x="40" y="690" width="236" height="447" rx="40" fill="url(#suitGrad)" role="img" aria-label="Product photo of a black EMS electrostimulation suit with blue trim"/>
    <path d="M290,923 H852 M409,923 V946 M636,923 V946 M852,923 V946" stroke="#555" stroke-width="2" fill="none"/>
    <g fill="var(--icon-grey)">
      <circle cx="409" cy="996" r="41"/>
      <circle cx="636" cy="996" r="41"/>
      <circle cx="857" cy="996" r="41"/>
    </g>
    <g fill="#fff" stroke="none">
      <path d="M390,1018 C388,990 405,972 432,970 C432,996 418,1014 390,1018 Z"/>
      <path d="M618,992 h8 v26 h-8 Z M629,992 l10,-18 c5,0 7,4 6,9 l-2,8 h14 c4,0 7,4 6,8 l-4,16 c-1,3 -3,5 -6,5 h-24 Z"/>
      <path d="M838,998 h26 l-8,-9 l4,-4 l16,15 l-16,15 l-4,-4 l8,-9 h-26 Z"/>
    </g>
    <g stroke="#fff" stroke-width="3" stroke-linecap="round">
      <path d="M828,986 h10 M824,996 h8 M828,1006 h10"/>
    </g>
    <path d="M40,1270 Q490,1060 940,1270 Z" fill="url(#plumGrad)"/>
  </svg>

  <div class="abs brand-mark">
    <span class="brand-dot"></span>
    <span class="brand-name">Wenna's Atelier</span>
  </div>

  <h1 class="abs headline"><span class="line-a">WENNA'S ATELIER NEW BUSINESS</span><span class="line-b">in Verbier, Switzerland</span></h1>

  <p class="abs offer-lead">Wenna's Atelier<br>offers that is</p>
  <p class="abs ems-word">EMS</p>
  <p class="abs ems-full">Electric Muscle<br>Stimulation</p>

  <p class="abs festival-title">A BIKE FESTIVAL IN VERBIER ION</p>
  <p class="abs festival-name">Alpen Pedal Gathering</p>
  <p class="abs festival-note">take an opportunity of this slot to advertise our<br>new suit of EMS that can be very helpful for bike riders.</p>

  <p class="abs feature" style="left:299px">The product is a<br>suit with muscle<br>electrostimulation</p>
  <p class="abs feature" style="left:526px">There are many<br>advantages<br>and functionnality</p>
  <p class="abs feature" style="left:747px">For sportsmen<br>and women,<br>it can</p>

  <p class="abs site-url">www.wenna-atelier.example</p>
</div>
</body>
</html>
```